Business Card Design - Pelrina

Please see our website www.pelrina.com.au

We supply high quality natural therapeutic medications to animal health care providers such as Veterinary clinics & saddlery stores.

Our main product we distribute is Gorvadine for horses, dogs and cats, which is an arthritis supplement.

Feel free to use images below in the design we have the rights to use them.

A quote for the job would be great too please.

It would be good to stick with the colour theme of our website if possible please.

Thanks,

Dan
Updates

Hi Folks, Apologies, I made a mistake with the contact no. in the opening brief. It should be 0491 583 162 (not 0491 726 934 which is my private practice office number.) Thanks for your submissions, much appreciated and several under serious consideration, Dan

Target Market(s)

Veterinary clinics, saddlery stores, produce stores.

Industry/Entity Type

Health

Contact Information for Business Card

orders@pelrina.net
www.pelrina.com.au
ph. 0491 583 162
ABN 47 209 615 883 (SMALL SIZE)

Colors
b768aa

Requirements
Should not have
• My name (Dr Dan Harcourt)

```html
<!DOCTYPE html>
<html lang="en">
<head>
<meta charset="utf-8">
<title>Pelrina Business Card</title>
<link rel="stylesheet" href="https://fonts.googleapis.com/css2?family=Open+Sans:wght@400;700;800&display=swap">
<style>
  :root {
    --stage-light: #ffffff;
    --stage-dark: #070707;
    --card-magenta: #ff12e6;
    --card-purple: #b60af2;
    --card-blue: #5b12f2;
    --frame-black: #000000;
    --brand-yellow: #fff200;
    --paw-yellow: #f7ee1c;
    --paw-cyan: #19e6f2;
    --text-white: #ffffff;
    --photo-light: #eef3f2;
    --photo-mid: #b9cfe6;
    --photo-warm: #d9b98a;
  }
  * { margin: 0; padding: 0; box-sizing: border-box; }
  html, body {
    width: 1200px;
    height: 848px;
    overflow: hidden;
  }
  body {
    position: relative;
    font-family: "Open Sans", Arial, sans-serif;
  }
  .stage {
    position: absolute;
    left: 0;
    width: 1200px;
    height: 424px;
  }
  .stage--light { top: 0; background: var(--stage-light); }
  .stage--dark { top: 424px; background: var(--stage-dark); }

  .card {
    position: absolute;
    left: 307px;
    top: 32px;
    width: 585px;
    height: 360px;
    overflow: hidden;
  }
  .card__art {
    position: absolute;
    inset: 0;
    width: 585px;
    height: 360px;
    display: block;
  }
  .card__brand {
    position: absolute;
    left: 352px;
    top: 97px;
    font-weight: 800;
    font-size: 31px;
    line-height: 1;
    color: var(--brand-yellow);
    letter-spacing: 0.2px;
  }
  .card__brand-dot {
    position: absolute;
    left: 456px;
    top: 58px;
    width: 30px;
    height: 30px;
    border-radius: 50%;
    background: var(--text-white);
  }
  .card__contact {
    position: absolute;
    right: 45px;
    top: 241px;
    text-align: right;
    color: var(--text-white);
    font-size: 15px;
    line-height: 17.6px;
    font-weight: 400;
  }
  .sprite { position: absolute; width: 0; height: 0; }
</style>
</head>
<body>

<svg class="sprite" aria-hidden="true">
  <defs>
    <symbol id="paw-icon" viewBox="0 0 20 20">
      <ellipse cx="10" cy="14" rx="5.6" ry="4.6"/>
      <ellipse cx="2.8" cy="8" rx="2.2" ry="2.8"/>
      <ellipse cx="7" cy="3.6" rx="2.2" ry="2.9"/>
      <ellipse cx="13" cy="3.6" rx="2.2" ry="2.9"/>
      <ellipse cx="17.2" cy="8" rx="2.2" ry="2.8"/>
    </symbol>
    <linearGradient id="photo-tone" x1="0" y1="0" x2="1" y2="1">
      <stop offset="0" stop-color="#dfeceb"/>
      <stop offset="0.45" stop-color="#b9cfe6"/>
      <stop offset="0.75" stop-color="#d9b98a"/>
      <stop offset="1" stop-color="#eef1f2"/>
    </linearGradient>
  </defs>
</svg>

<section class="stage stage--light">
  <article class="card">
    <svg class="card__art" viewBox="0 0 585 360">
      <rect width="585" height="360" fill="var(--card-magenta)"/>
      <polygon points="241,0 585,0 585,136 302,168" fill="var(--card-purple)"/>
      <polygon points="302,168 585,136 585,360 369,360" fill="var(--card-blue)"/>
      <polygon points="26,25 233,25 341,334 26,334" fill="url(#photo-tone)" stroke="var(--frame-black)" stroke-width="3" role="img" aria-label="Photo of a smiling veterinary nurse in blue scrubs holding a long-haired small dog on an examination table"/>
      <use href="#paw-icon" x="334" y="178" width="36" height="36" fill="var(--paw-yellow)" transform="rotate(-12 352 196)"/>
      <use href="#paw-icon" x="368" y="205" width="36" height="36" fill="var(--paw-cyan)" transform="rotate(-12 386 223)"/>
    </svg>
    <span class="card__brand-dot"></span>
    <div class="card__brand">Pelrina</div>
    <address class="card__contact" style="font-style:normal">
      orders@pelrina.net<br>
      www.pelrina.com.au<br>
      0491 583 162<br>
      ABN 47 209 615 883
    </address>
  </article>
</section>

<section class="stage stage--dark">
  <article class="card">
    <svg class="card__art" viewBox="0 0 585 360">
      <rect width="585" height="360" fill="var(--card-magenta)"/>
      <polygon points="241,0 585,0 585,136 302,168" fill="var(--card-purple)"/>
      <polygon points="302,168 585,136 585,360 369,360" fill="var(--card-blue)"/>
      <polygon points="26,25 233,25 341,334 26,334" fill="url(#photo-tone)" stroke="var(--frame-black)" stroke-width="3" role="img" aria-label="Photo of a smiling veterinary nurse in blue scrubs holding a long-haired small dog on an examination table"/>
      <use href="#paw-icon" x="334" y="178" width="36" height="36" fill="var(--paw-yellow)" transform="rotate(-12 352 196)"/>
      <use href="#paw-icon" x="368" y="205" width="36" height="36" fill="var(--paw-cyan)" transform="rotate(-12 386 223)"/>
    </svg>
    <span class="card__brand-dot"></span>
    <div class="card__brand">Pelrina</div>
    <address class="card__contact" style="font-style:normal">
      orders@pelrina.net<br>
      www.pelrina.com.au<br>
      0491 583 162<br>
      ABN 47 209 615 883
    </address>
  </article>
</section>

</body>
</html>
```